Business Card Design Project

I help solve problems that people have with real estate, so I buy homes for cash that they no longer want, can't afford, inherited, etc. and fix and sell them or rent them or take over mortgage payments. See website: www.quickdeedhomestead.com

Industry/Entity Type

Real Estate

Contact Information for Business Card

Not exactly sure. Looking for a design that either is similar to the website www.quickdeedhomestead.com or that reflects what I do as described below. If it can look a little luxurious to show I can buy the houses for cash and I fix them and sell them, it's a bonus. I seem to like some of the higher end things like foil or black or something that makes it stand out.

Font styles to use
Serif

Requirements
Nice to have
• I seem to like black or clear. I like things to stand out and be different.

```html
<!DOCTYPE html>
<html lang="en">
<head>
<meta charset="utf-8">
<title>Renewed Dwellings – Business Card</title>
<link rel="stylesheet" href="https://fonts.googleapis.com/css2?family=Roboto:wght@400;500;900&family=Open+Sans:wght@600&display=swap">
<style>
  :root {
    --bg: #e8e9e9;
    --green-light: #74c043;
    --green-mid: #559a3a;
    --green-dark: #3f7f38;
    --brand-green: #3a8a2e;
    --ink: #2f2f2f;
    --paper: #f7f7f7;
    --white: #ffffff;
  }
  * { margin: 0; padding: 0; box-sizing: border-box; }
  html, body { width: 1200px; height: 726px; overflow: hidden; }
  body {
    background: var(--bg);
    font-family: "Roboto", Arial, sans-serif;
    position: relative;
  }
  .card {
    position: absolute;
    top: 200px;
    width: 540px;
    height: 309px;
    border-radius: 3px;
    box-shadow: 0 6px 18px rgba(0,0,0,0.12);
    overflow: hidden;
  }
  .card--front {
    left: 40px;
    background: linear-gradient(160deg, var(--green-light) 0%, var(--green-mid) 50%, var(--green-dark) 100%);
    color: var(--white);
  }
  .card--back {
    left: 620px;
    background: var(--paper);
    color: var(--ink);
  }
  .brand-name {
    font-family: "Roboto", Arial, sans-serif;
    font-weight: 900;
    text-transform: uppercase;
    line-height: 0.95;
    letter-spacing: 1px;
  }
  .card--front .brand-name {
    position: absolute;
    left: 80px;
    top: 92px;
    font-size: 50px;
    color: var(--white);
  }
  .tagline {
    position: absolute;
    left: 0;
    right: 0;
    bottom: 40px;
    text-align: center;
    font-size: 15px;
    color: var(--white);
  }
  .card--back .brand-name {
    position: absolute;
    right: 34px;
    top: 34px;
    font-size: 30px;
    color: var(--brand-green);
    text-align: left;
  }
  .person {
    position: absolute;
    left: 36px;
    top: 150px;
  }
  .person__name {
    font-family: "Open Sans", Arial, sans-serif;
    font-weight: 600;
    font-size: 22px;
    color: var(--ink);
  }
  .person__role {
    font-size: 15px;
    color: var(--brand-green);
    margin-top: 2px;
  }
  .contact {
    position: absolute;
    left: 36px;
    bottom: 30px;
    list-style: none;
    font-size: 15px;
    line-height: 1.35;
  }
  .contact__item { display: flex; align-items: center; gap: 10px; }
  .contact__icon { width: 14px; height: 14px; fill: var(--brand-green); flex: none; }
  .contact__accent { color: var(--brand-green); }
</style>
</head>
<body>
  <section class="card card--front" aria-label="Card front">
    <div class="brand-name">Renewed<br>Dwellings</div>
    <p class="tagline">Selling and Buying Houses in Illinois</p>
  </section>

  <section class="card card--back" aria-label="Card back">
    <div class="brand-name">Renewed<br>Dwellings</div>
    <div class="person">
      <p class="person__name">Jordan Avery Blake</p>
      <p class="person__role">Managing Director</p>
    </div>
    <ul class="contact">
      <li class="contact__item">
        <svg class="contact__icon" viewBox="0 0 16 16" aria-hidden="true"><path d="M3 1h3l1.5 4-2 1.3a9 9 0 0 0 4.2 4.2L11 8.5l4 1.5v3a2 2 0 0 1-2 2A12 12 0 0 1 1 3a2 2 0 0 1 2-2z"/></svg>
        <span>555-014-<span class="contact__accent">SOLD</span></span>
      </li>
      <li class="contact__item">
        <svg class="contact__icon" viewBox="0 0 16 16" aria-hidden="true"><path d="M1 3h14v10H1z M1 3l7 6 7-6" fill="var(--brand-green)" stroke="var(--paper)" stroke-width="1.2"/></svg>
        <span>jordan@quickdeedhomestead.com</span>
      </li>
      <li class="contact__item">
        <svg class="contact__icon" viewBox="0 0 16 16" aria-hidden="true"><circle cx="8" cy="8" r="7"/><path d="M1 8h14M8 1c-3 3.5-3 10.5 0 14M8 1c3 3.5 3 10.5 0 14" fill="none" stroke="var(--paper)" stroke-width="1"/></svg>
        <span>www.quickdeedhomestead.com</span>
      </li>
    </ul>
  </section>
</body>
</html>
```